Business Card Design Project

I am seeking a business card for my life coaching career. I specialize in coaching executives and entrepreneurs. Consciousness plays a key role in my practice.
Updates

I would like to see different fonts -I don't like the way the capital J looks. I only want my name once on the card, on the front. I like everything centered on the front, with a white background, grey and green on the front; and the same grey on the back with bullet points next to each quality; centered. I like a subtle shadow of the mountains behind the text on the back of the card. I don't want the mountains on either side to be too big. Thank you.

Target Market(s)

Middle age business owners/executives

Industry/Entity Type

Business

Contact Information for Business Card

The front design is my name and a mountain logo. I want to have my name prominently shown.

Requirements
Must have
• Front of card:
• My name prominent sized font
• Helping clients lead more fulfilling lives;
• Executive Life Coach
• 415-362-4807
• pkrelt4@mailvane.net
• Back of Card:
• Providing Unparalleled support
• Providing a safe place to grow in self-awareness
• 20+ years entrepreneurial experience
• Trust
• Integrity
Nice to have
• Easy to read font; warm colors reflecting a masculine personality.

```html
<!DOCTYPE html>
<html lang="en">
<head>
<meta charset="utf-8">
<title>Owen Hartley – Business Card</title>
<link rel="stylesheet" href="https://fonts.googleapis.com/css2?family=Mulish:wght@400;600;700;800&display=swap">
<style>
  :root {
    --canvas: #f1f1f1;
    --paper: #ffffff;
    --green: #5f7c45;
    --green-light: #6b8950;
    --charcoal: #4a4646;
    --charcoal-dark: #3f3b3b;
    --ink: #3a3a3a;
    --white: #ffffff;
  }
  * { box-sizing: border-box; margin: 0; padding: 0; }
  html, body {
    width: 1200px; height: 1000px; overflow: hidden;
    background: var(--canvas);
    font-family: "Mulish", "Century Gothic", sans-serif;
  }
  .card {
    position: absolute; top: 313px;
    width: 547px; height: 313px;
    overflow: hidden;
    box-shadow: 0 1px 3px rgba(0,0,0,0.12);
  }
  .card--front { left: 43px; background: var(--paper); }
  .card--back { left: 614px; width: 549px; background: var(--charcoal); }

  .front-shapes { position: absolute; inset: 0; }

  .brand {
    position: absolute; left: 20px; top: 140px; width: 240px;
    text-align: center;
  }
  .brand__name {
    font-size: 35px; font-weight: 800; color: var(--green);
    letter-spacing: -0.3px; line-height: 1;
  }
  .brand__tagline {
    margin-top: 6px;
    font-size: 9.5px; font-weight: 800; color: var(--ink);
    letter-spacing: 0.6px; word-spacing: 2px;
  }

  .identity {
    position: absolute; right: 23px; top: 24px; text-align: right; color: var(--white);
  }
  .identity__name { font-size: 22px; font-weight: 700; letter-spacing: 0.8px; line-height: 1.1; }
  .identity__title { font-size: 13.5px; font-weight: 400; letter-spacing: 0.3px; margin-top: 2px; }

  .contact {
    position: absolute; right: 20px; top: 250px;
    list-style: none; color: var(--white); text-align: right;
    font-size: 15px; line-height: 23px;
  }
  .contact li { display: flex; justify-content: flex-end; align-items: center; gap: 4px; }
  .contact svg { width: 14px; height: 14px; }

  .values {
    position: absolute; left: 0; right: 0; top: 86px;
    list-style: none; text-align: center; color: var(--white);
    font-size: 15.5px; line-height: 28.5px; letter-spacing: 0.2px;
  }
</style>
</head>
<body>

<section class="card card--front" aria-label="Front of business card">
  <svg class="front-shapes" viewBox="0 0 547 313" width="547" height="313" aria-hidden="true">
    <defs>
      <radialGradient id="greenField" cx="0.7" cy="0.45" r="0.7">
        <stop offset="0" stop-color="var(--green-light)"/>
        <stop offset="1" stop-color="var(--green)"/>
      </radialGradient>
    </defs>
    <path d="M277 0 C340 60 345 230 192 313 L547 313 L547 0 Z" fill="var(--charcoal)"/>
    <path d="M294 0 C352 70 358 225 258 313 L547 313 L547 0 Z" fill="url(#greenField)"/>
    <path d="M270 82 C290 140 288 215 262 275 C282 220 288 150 270 82 Z" fill="var(--paper)" stroke="var(--charcoal)" stroke-width="2"/>
    <path d="M325 225 C310 265 285 292 258 313 L268 313 C295 290 316 262 325 225 Z" fill="var(--charcoal)"/>
  </svg>

  <div class="brand">
    <p class="brand__name">Owen Hartley</p>
    <p class="brand__tagline">Helping Clients lead more fulfilling lives</p>
  </div>

  <div class="identity">
    <h1 class="identity__name">OWEN HARTLEY</h1>
    <p class="identity__title">Executive Life Coach</p>
  </div>

  <ul class="contact">
    <li>415-362-4807
      <svg viewBox="0 0 14 14" aria-hidden="true"><circle cx="7" cy="7" r="6.2" fill="none" stroke="#fff" stroke-width="1.1"/><path d="M4.6 3.8 L5.8 3.6 L6.4 5.2 L5.6 5.9 C6 6.9 6.9 7.8 7.9 8.3 L8.6 7.5 L10.2 8.1 L10 9.3 C7.2 9.6 4.3 6.7 4.6 3.8 Z" fill="#fff"/></svg>
    </li>
    <li>pkrelt4@mailvane.net
      <svg viewBox="0 0 14 14" aria-hidden="true"><circle cx="7" cy="7" r="6.5" fill="#fff"/><rect x="3.6" y="4.6" width="6.8" height="4.8" fill="none" stroke="var(--green)" stroke-width="1"/><path d="M3.8 4.8 L7 7.4 L10.2 4.8" fill="none" stroke="var(--green)" stroke-width="1"/></svg>
    </li>
  </ul>
</section>

<section class="card card--back" aria-label="Back of business card">
  <ul class="values">
    <li>Trust</li>
    <li>Integrity</li>
    <li>Providing Unparalleled support</li>
    <li>20+ years entrepreneurial experience</li>
    <li>Providing a safe place to grow in self-awareness</li>
  </ul>
</section>

</body>
</html>
```